Webdesign für Anbieter von Erotik-Geschichten
Zielgruppe
Wir sind ein Anbieter von Erotik-Geschichten. Die Marke heisst Vosk Erotica. Das Erlebnis für die Kunden soll hochwertig und persönlich wirken. Daher in keiner Art und Weise schmuddelig. Die Zielgruppe sind Frauen ab ca. 20-40. Die Geschichten werden frei lesbar sein, d.h. es ist kein Online-Shop sondern mehr eine Art Blog mit verschiedenen Geschichten.
Aufgabenstellung
Wichtig ist uns eine schlichtes, minimalistisches Design (vrgl. Faltblatt) aber trotzdem hochwertig (leicht luxuriös) wirkend.

```html
<!DOCTYPE html>
<html lang="de">
<head>
<meta charset="utf-8">
<title>Vosk – Erotische Kurzgeschichten</title>
<link href="https://fonts.googleapis.com/css2?family=Bitter:wght@400;500;600;700&family=Open+Sans:wght@400;600&display=swap" rel="stylesheet">
<style>
  :root {
    --bg: #333333;
    --header: #2e2e2e;
    --card: #5a5a5a;
    --text: #ffffff;
    --muted: #e6e6e6;
    --accent: #e0281f;
  }
  * { margin: 0; padding: 0; box-sizing: border-box; }
  html, body { width: 1200px; height: 2718px; overflow: hidden; }
  body {
    position: relative;
    background: var(--bg);
    color: var(--text);
    font-family: "Open Sans", sans-serif;
  }
  .serif { font-family: "Bitter", serif; }

  /* Header */
  .site-header {
    position: absolute; left: 0; top: 0; width: 1200px; height: 116px;
    background: var(--header);
  }
  .brand {
    position: absolute; left: 74px; top: 38px;
    font-family: "Bitter", serif; font-size: 38px; font-weight: 500; color: var(--text);
  }
  .main-nav { position: absolute; left: 252px; top: 53px; display: flex; gap: 34px; }
  .main-nav a, .footer-nav a {
    font-family: "Bitter", serif; font-size: 14px; font-weight: 500;
    color: var(--text); text-decoration: none; letter-spacing: .4px;
  }
  .main-nav a.active { color: var(--accent); }
  .header-tools { position: absolute; left: 838px; top: 44px; display: flex; align-items: center; gap: 20px; }
  .header-tools svg { width: 17px; height: 17px; fill: var(--accent); }
  .btn-upgrade {
    margin-left: 10px; width: 115px; height: 34px; border: 2px solid var(--accent); border-radius: 17px;
    font-family: "Bitter", serif; font-weight: 600; font-size: 15px; color: var(--accent);
    display: flex; align-items: center; justify-content: center;
  }
  .avatar {
    width: 38px; height: 38px; border-radius: 50%; border: 2px solid var(--accent);
    background: radial-gradient(circle at 50% 45%, #c98a6c, #6a3b2c);
  }

  /* Hero */
  .hero {
    position: absolute; left: 0; top: 116px; width: 1200px; height: 463px;
    background: linear-gradient(90deg, #2f3033 0%, #4a4d55 30%, #8a6a55 55%, #b98a6a 70%, #c9c4c0 88%, #d9d6d2 100%);
  }
  .hero h1 {
    position: absolute; left: 76px; top: 128px; width: 620px;
    font-family: "Bitter", serif; font-weight: 400; font-size: 57px; line-height: 56px;
  }

  /* Intro */
  .intro { position: absolute; left: 83px; top: 635px; width: 600px; }
  .intro h2, .categories h2 { font-family: "Bitter", serif; font-weight: 400; font-size: 21px; margin-bottom: 14px; }
  .intro p { font-size: 14px; line-height: 24.5px; color: var(--muted); margin-bottom: 16px; }
  .categories { position: absolute; left: 771px; top: 635px; width: 280px; }
  .categories h2 { margin-bottom: 16px; }
  .tag-list { display: flex; flex-wrap: wrap; gap: 13px 8px; width: 270px; }
  .tag {
    height: 27px; padding: 0 22px; border: 2px solid var(--accent); border-radius: 14px;
    font-family: "Bitter", serif; font-weight: 600; font-size: 10.5px; color: var(--accent);
    display: flex; align-items: center;
  }
  .tag-list .break { flex-basis: 100%; height: 0; margin: -13px 0 0; }

  /* Stories */
  .stories-title {
    position: absolute; left: 0; top: 895px; width: 1200px; text-align: center;
    font-family: "Bitter", serif; font-weight: 400; font-size: 40px;
  }
  .filters { position: absolute; left: 353px; top: 968px; display: flex; gap: 17px; }
  .filter {
    width: 154px; height: 34px; border: 2px solid var(--text); border-radius: 17px;
    font-family: "Bitter", serif; font-weight: 600; font-size: 14px;
    display: flex; align-items: center; justify-content: center; gap: 12px;
  }
  .filter svg { width: 14px; height: 10px; stroke: var(--text); stroke-width: 2.5; fill: none; }

  .story-grid {
    position: absolute; left: 75px; top: 1071px;
    display: grid; grid-template-columns: 340px 340px 341px; column-gap: 16px; row-gap: 28px;
  }
  .story-card { height: 298px; background: var(--card); padding: 24px 34px 0; position: relative; }
  .story-card .category { font-size: 14px; color: var(--muted); margin-bottom: 9px; }
  .story-card h3 { font-family: "Bitter", serif; font-weight: 400; font-size: 21px; line-height: 20px; margin-bottom: 12px; }
  .story-card p { font-size: 14px; line-height: 22.5px; color: var(--muted); }
  .read-more {
    position: absolute; left: 28px; top: 236px; width: 137px; height: 35px;
    border: 2px solid var(--accent); border-radius: 18px;
    font-family: "Bitter", serif; font-weight: 600; font-size: 14px; color: var(--accent);
    display: flex; align-items: center; justify-content: center;
  }

  .load-more {
    position: absolute; left: 418px; top: 2402px; width: 364px; height: 44px;
    border: 2px solid var(--text); border-radius: 22px;
    font-family: "Bitter", serif; font-weight: 600; font-size: 20px;
    display: flex; align-items: center; justify-content: center;
  }

  /* Footer */
  .site-footer {
    position: absolute; left: 0; top: 2519px; width: 1200px; height: 199px;
    border-top: 2px solid var(--accent); background: var(--header);
  }
  .footer-nav { position: absolute; left: 405px; top: 26px; display: flex; gap: 34px; }
  .footer-brand {
    position: absolute; left: 0; top: 68px; width: 1200px; text-align: center;
    font-family: "Bitter", serif; font-size: 52px; font-weight: 500;
  }
  .legal { position: absolute; left: 364px; top: 174px; display: flex; gap: 56px; font-size: 11px; font-weight: 600; color: #bdbdbd; }
  .legal a { color: #bdbdbd; }
</style>
</head>
<body>

<header class="site-header">
  <div class="brand">Vosk</div>
  <nav class="main-nav">
    <a class="active" href="#">HOME</a>
    <a href="#">KATEGORIEN</a>
    <a href="#">AUTOREN</a>
    <a href="#">ÜBER UNS</a>
  </nav>
  <div class="header-tools">
    <svg viewBox="0 0 24 24" aria-label="Suche"><path d="M10 2a8 8 0 0 1 6.3 12.9l5.4 5.4-2.1 2.1-5.4-5.4A8 8 0 1 1 10 2zm0 3a5 5 0 1 0 0 10 5 5 0 0 0 0-10z"/></svg>
    <svg viewBox="0 0 24 24" aria-label="Merkliste"><path d="M5 2h14v20l-7-5-7 5z"/></svg>
    <svg viewBox="0 0 24 24" aria-label="Benachrichtigungen"><path d="M12 2a6 6 0 0 1 6 6v6l2 3H4l2-3V8a6 6 0 0 1 6-6zm-2.5 17h5a2.5 2.5 0 0 1-5 0z"/></svg>
    <div class="btn-upgrade">Upgrade</div>
    <div class="avatar" role="img" aria-label="Profilbild"></div>
  </div>
</header>

<section class="hero" role="img" aria-label="Foto einer Frau in dunklem Body, sitzend an einer hellen Wand">
  <h1>Erotische Kurzgeschichten von Frauen für Frauen</h1>
</section>

<section class="intro">
  <h2>Willkommen bei Vosk</h2>
  <p>Lorem ipsum dolor sit amet, consectetuer adipiscing elit. Aenean commodo ligula eget dolor. Aenean massa. Cum sociis natoque penatibus et magnis dis parturient montes, nascetur ridiculus mus. Donec quam felis.</p>
  <p>Nullam dictum felis eu pede mollis pretium. Integer tincidunt. Cras dapibus. Vivamus elementum semper nisi. Aenean vulpnean leo ligula, porttitor&nbsp; eu, consequat vitae.</p>
</section>

<aside class="categories">
  <h2>Kategorien</h2>
  <div class="tag-list">
    <span class="tag">Alleine</span><span class="tag">Arbeitsplatz</span><span class="break"></span>
    <span class="tag">Schule</span><span class="tag">Ferien</span><span class="tag">BDSM</span><span class="break"></span>
    <span class="tag">Dreier</span><span class="tag">Lesbisch</span><span class="break"></span>
    <span class="tag">Sugar / Escort</span><span class="tag">Step</span>
  </div>
</aside>

<h2 class="stories-title">Neue Geschichten bei Vosk</h2>
<div class="filters">
  <div class="filter">Sortiert nach <svg viewBox="0 0 14 10"><path d="M2 2l5 5 5-5"/></svg></div>
  <div class="filter">Kategorie <svg viewBox="0 0 14 10"><path d="M2 2l5 5 5-5"/></svg></div>
  <div class="filter">Autor <svg viewBox="0 0 14 10"><path d="M2 2l5 5 5-5"/></svg></div>
</div>

<main class="story-grid">
  <article class="story-card"><div class="category">Ferien</div><h3>Nächte in Samt und Seide</h3><p>Lorem ipsum dolor sit amet, consectetuer adipiscing elit. Aenean commodo ligula eget dolor. Aenean massa. Cum sociis natoque penatibus et magnis dis parturient montes, nascetur ridiculus mus.</p><div class="read-more">Weiterlesen</div></article>
  <article class="story-card"><div class="category">Arbeitsplatz</div><h3>Der Fremde im Zimmer nebenan</h3><p>Lorem ipsum dolor sit amet, consectetuer adipiscing elit. Aenean commodo ligula eget dolor. Aenean massa. Cum sociis natoque penatibus et magnis dis parturient.</p><div class="read-more">Weiterlesen</div></article>
  <article class="story-card"><div class="category">Alleine</div><h3 style="margin-bottom:32px">Foodporn</h3><p>Lorem ipsum dolor sit amet, consectetuer adipiscing elit. Aenean commodo ligula eget dolor. Aenean massa. Cum sociis natoque penatibus et magnis dis parturient.</p><div class="read-more">Weiterlesen</div></article>

  <article class="story-card"><div class="category">BDSM</div><h3>Die Flitterwochen</h3><p>Donec pede justo, fringilla vel, aliquet nec, vulputate eget, arcu. In enim justo, rhoncus ut, imperdiet a, venenatis vitae, justo. Nullam dictum felis eu pede mollis pretium.</p><div class="read-more">Weiterlesen</div></article>
  <article class="story-card"><div class="category">Alleine</div><h3>Spass allein</h3><p>Donec pede justo, fringilla vel, aliquet nec, vulputate eget, arcu. In enim justo, rhoncus ut, imperdiet a, venenatis vitae, justo. Nullam dictum felis eu pede mollis pretium.</p><div class="read-more">Weiterlesen</div></article>
  <article class="story-card"><div class="category">Lesbisch</div><h3>Die beste Freundin</h3><p>Donec pede justo, fringilla vel, aliquet nec, vulputate eget, arcu. In enim justo, rhoncus ut, imperdiet a, venenatis vitae, justo. Nullam dictum felis eu pede mollis pretium.</p><div class="read-more">Weiterlesen</div></article>

  <article class="story-card"><div class="category">Ferien</div><h3>Die Urlaubsbekanntschaft</h3><p>Donec pede justo, fringilla vel, aliquet nec, vulputate eget, arcu. In enim justo, rhoncus ut, imperdiet a, venenatis vitae, justo. Nullam dictum felis eu pede mollis pretium.</p><div class="read-more">Weiterlesen</div></article>
  <article class="story-card"><div class="category">Ferien</div><h3>Quicky am Strand</h3><p>Donec pede justo, fringilla vel, aliquet nec, vulputate eget, arcu. In enim justo, rhoncus ut, imperdiet a, venenatis vitae, justo. Nullam dictum felis eu pede mollis pretium.</p><div class="read-more">Weiterlesen</div></article>
  <article class="story-card"><div class="category">Schule</div><h3>Die Wette</h3><p>Donec pede justo, fringilla vel, aliquet nec, vulputate eget, arcu. In enim justo, rhoncus ut, imperdiet a, venenatis vitae, justo. Nullam dictum felis eu pede mollis pretium.</p><div class="read-more">Weiterlesen</div></article>

  <article class="story-card"><div class="category">Dreier</div><h3>Ménage à trois</h3><p>Donec pede justo, fringilla vel, aliquet nec, vulputate eget, arcu. In enim justo, rhoncus ut, imperdiet a, venenatis vitae, justo. Nullam dictum felis eu pede mollis pretium.</p><div class="read-more">Weiterlesen</div></article>
  <article class="story-card"><div class="category">Ferien</div><h3>Der Fremde in meinem Bett</h3><p>Donec pede justo, fringilla vel, aliquet nec, vulputate eget, arcu. In enim justo, rhoncus ut, imperdiet a, venenatis vitae, justo. Nullam dictum felis eu pede mollis pretium.</p><div class="read-more">Weiterlesen</div></article>
  <article class="story-card"><div class="category">Sugar / Escort</div><h3>Mit Finanziellem Interesse</h3><p>Donec pede justo, fringilla vel, aliquet nec, vulputate eget, arcu. In enim justo, rhoncus ut, imperdiet a, venenatis vitae, justo. Nullam dictum felis eu pede mollis pretium.</p><div class="read-more">Weiterlesen</div></article>
</main>

<div class="load-more">Mehr Geschichten laden</div>

<footer class="site-footer">
  <nav class="footer-nav">
    <a href="#">HOME</a>
    <a href="#">KATEGORIEN</a>
    <a href="#">AUTOREN</a>
    <a href="#">ÜBER UNS</a>
  </nav>
  <div class="footer-brand">Vosk</div>
  <div class="legal">
    <span>© Vosk GmbH 2021</span>
    <a href="#">Impressum</a>
    <a href="#">AGB</a>
    <a href="#">Datenschutz</a>
  </div>
</footer>

</body>
</html>
```